Hollowmere Farm Promotional Leaflet

The team at Hollowmere Farm can help with every aspect of managing and enhancing your home from housekeeping and professional cleaning, laundry and ironing to providing chic and contemporary flower arrangements and even food for your pets!We take pride in providing high-end, consistent and reliable professional services bespoke to you. Whether you are a busy professional working long hours, a stay-at home parent or retired; having professional help in the home gives you time to spend on the things you enjoy.We are providing a very upmarket, highly professional service and need an A5 promotional leaflet to be designed. Please refer to www.hollowmerefarm.example.co.uk and see the section on 'Home Management'The leaflet should incorporate the Hollowmere Farm logo without the 'tipi', and any suitable photography images used on the home page of the website or the 'home management' section.

Target Market(s)

high-end, affluent owners of luxury homes

Industry/Entity Type

Farm

Contact Information for Business Card

The business card design needs to be suitable for use across all of Hollowmere Farm businesses, specifically:
Hollowmere Farm Home Management - otherwise known as Hollowmere Farm @ Home (this uses the typographical logo
Hollowmere Farm Weddings & Events - this uses the 'tipi' logo

Requirements
Must have
• Design in keeping with the look and feel of the logo and website design
• www.hollowmerefarm.example.co.uk

```html
<!DOCTYPE html>
<html lang="en">
<head>
<meta charset="utf-8">
<title>Hollowmere Farm – Home Management Leaflet</title>
<link rel="stylesheet" href="https://fonts.googleapis.com/css2?family=Open+Sans:ital,wght@0,400;0,600;0,700;1,400;1,600&family=Pinyon+Script&family=Cormorant+Garamond:ital,wght@0,500;0,600;1,600&display=swap">
<style>
  :root {
    --backdrop: #2a2a2a;
    --magenta: #d6225f;
    --magenta-deep: #b81a52;
    --plum: #5a1230;
    --gold: #e0b65a;
    --gold-tile: #dcb35e;
    --pink-soft: #f37fb3;
    --grey-panel: #e3e3e3;
    --grey-light: #efefef;
    --blush: #f6e4ea;
    --ink: #4a4a4a;
    --white: #ffffff;
  }
  * { box-sizing: border-box; margin: 0; padding: 0; }
  html, body { width: 1200px; height: 961px; overflow: hidden; background: var(--backdrop); }
  .canvas { position: relative; width: 1200px; height: 961px; }

  .page { position: absolute; top: 134px; width: 489px; height: 694px; overflow: hidden;
          box-shadow: 0 6px 18px rgba(0,0,0,.55); }
  .page--front { left: 96px; background: var(--magenta); }
  .page--back { left: 615px; background: var(--grey-panel); }

  /* Front */
  .masthead { position: absolute; left: 0; top: 0; width: 100%; height: 145px;
              display: flex; align-items: center; justify-content: center; gap: 12px; }
  .masthead__mark { width: 14px; height: 14px; border-radius: 50%; background: var(--gold); }
  .masthead__name { font-family: "Open Sans", sans-serif; font-weight: 600; font-size: 34px;
                    letter-spacing: 3px; color: var(--pink-soft); }

  .hero-photo { position: absolute; left: 0; top: 145px; width: 100%; height: 549px;
                background: linear-gradient(180deg, #2c4f9c 0%, #7a5a8a 22%, #c9773c 45%, #8e4a22 70%, #3a2218 100%); }
  .hero-title { position: absolute; left: 0; top: 205px; width: 100%; text-align: center;
                font-family: "Pinyon Script", cursive; color: var(--white); font-size: 50px; line-height: 68px;
                text-shadow: 0 2px 6px rgba(0,0,0,.7); }

  .front-base { position: absolute; left: 0; bottom: 0; width: 100%; height: 260px; }

  .intro-box { position: absolute; left: 18px; top: 450px; width: 455px; height: 228px;
               background: rgba(74,14,40,.88); border: 2px solid rgba(224,182,90,.6);
               border-radius: 18px 18px 18px 18px; padding: 14px 18px 0 20px;
               font-family: "Open Sans", sans-serif; color: var(--white); }
  .intro-box__heading { font-weight: 700; font-size: 13px; color: var(--gold); margin-top: 4px; }
  .intro-box__heading:first-child { margin-top: 0; }
  .intro-box__text { font-size: 10.6px; line-height: 14px; margin-bottom: 5px; }

  /* Back */
  .band { position: absolute; left: 0; width: 100%; background: var(--magenta);
          display: flex; align-items: center; justify-content: center;
          font-family: "Cormorant Garamond", serif; font-style: italic; font-weight: 600;
          font-size: 21px; color: var(--white); }
  .band--cleaning { top: 0; height: 51px; }
  .band--services { top: 222px; height: 52px; }

  .cleaning { position: absolute; left: 0; top: 51px; width: 100%; height: 171px; background: var(--grey-light); }
  .cleaning__lead { position: absolute; left: 20px; top: 14px; width: 210px;
                    font-family: "Open Sans", sans-serif; font-size: 10.5px; line-height: 14px; color: var(--ink); }
  .cleaning__list { position: absolute; left: 20px; top: 62px; list-style: none;
                    font-family: "Open Sans", sans-serif; font-size: 10.5px; line-height: 13.7px; color: var(--ink); }
  .cleaning__list li::before { content: "•"; color: var(--magenta); margin-right: 6px; }
  .cleaning__photo { position: absolute; left: 367px; top: 15px; width: 103px; height: 137px;
                     border-radius: 8px; background: linear-gradient(160deg, #3b3430, #a89a86 55%, #5d5148); }

  .services { position: absolute; left: 0; top: 274px; width: 100%; height: 268px;
              background: linear-gradient(180deg, var(--grey-panel), #d6d6d6); }
  .tile { position: absolute; width: 144px; box-shadow: 0 4px 6px rgba(0,0,0,.25); }
  .tile__label { height: 24px; background: var(--gold-tile); display: flex; align-items: center; justify-content: center;
                 font-family: "Open Sans", sans-serif; font-style: italic; font-size: 9px; color: var(--magenta-deep); }
  .tile__photo { height: 79px; border: 2px solid var(--white); border-top: none; }

  .contact-area { position: absolute; left: 0; top: 542px; width: 100%; height: 152px; background: var(--blush); }
  .contact { position: absolute; left: 15px; top: 23px; width: 455px; height: 106px;
             border: 1.5px solid var(--magenta); border-radius: 18px; text-align: center;
             font-family: "Cormorant Garamond", serif; color: var(--ink); }
  .contact__tag { position: absolute; left: 50%; top: -9px; transform: translateX(-50%);
                  background: var(--magenta); color: var(--white); font-size: 12px; font-weight: 600;
                  letter-spacing: .5px; padding: 0 10px; border-radius: 8px; line-height: 16px; }
  .contact__address { margin-top: 14px; font-size: 12.5px; line-height: 14px; font-weight: 600; }
  .contact__phone { margin-top: 8px; font-size: 17px; font-weight: 600; }
  .contact__web { margin-top: 6px; font-size: 12px; font-weight: 600; letter-spacing: .3px; }
  .contact__web span { color: var(--magenta); }
</style>
</head>
<body>
<main class="canvas">

  <section class="page page--front">
    <header class="masthead">
      <span class="masthead__mark"></span>
      <span class="masthead__name">Hollowmere Farm</span>
    </header>

    <div class="hero-photo" role="img" aria-label="Evening festival wedding reception under a lit tipi with guests at long tables"></div>
    <svg class="front-base" viewBox="0 0 489 260" preserveAspectRatio="none" aria-hidden="true">
      <path d="M0 0 L22 40 Q40 60 90 60 L400 60 Q450 60 470 40 L489 0 L489 260 L0 260 Z" fill="#d6225f"/>
    </svg>
    <h1 class="hero-title">Home Management<br>Parties and<br>Festival Weddings</h1>

    <article class="intro-box">
      <h2 class="intro-box__heading">Home Management</h2>
      <p class="intro-box__text">The team at Hollowmere Farm can help with every aspect of managing &amp; enhancing your home from housekeeping and professional cleaning, laundry and ironing to providing chic and contemporary flower arrangements and even food for your</p>
      <h2 class="intro-box__heading">Parties &amp; Events</h2>
      <p class="intro-box__text">Whether you are planning a festival themed birthday party at home, an anniversary dinner party or a cocktail party, we can help you with creative ideas, meticulous event planning and access to the best local suppliers.</p>
      <h2 class="intro-box__heading">Festival Weddings</h2>
      <p class="intro-box__text">Do you dream of holding a bespoke “wedding fest” to rival Brackenfield? If you love the idea of a festival wedding day, Hollowmere Farm can provide the space and scope to create a unique celebration.</p>
    </article>
  </section>

  <section class="page page--back">
    <h2 class="band band--cleaning">Professional Cleaning Services</h2>
    <div class="cleaning">
      <p class="cleaning__lead">Coming home to a beautiful environment and be able to relax and enjoy your time is something we all deserve.</p>
      <ul class="cleaning__list">
        <li>Satisfaction guaranteed</li>
        <li>Professional staff you can trust and rely on</li>
        <li>Competitive rates</li>
        <li>CRB checked and referenced</li>
        <li>Member of the Household Staffing Guild</li>
        <li>Fully Insured</li>
        <li>Staff you can trust</li>
      </ul>
      <div class="cleaning__photo" role="img" aria-label="Elegant hallway with chandelier and staircase"></div>
    </div>

    <h2 class="band band--services">Home Management Services</h2>
    <div class="services">
      <div class="tile" style="left:18px;top:22px">
        <div class="tile__label">Professional Cleaning</div>
        <div class="tile__photo" role="img" aria-label="Bright living room with sofas" style="background:linear-gradient(180deg,#8e8a84,#d8d4ce 60%,#5e5a55)"></div>
      </div>
      <div class="tile" style="left:171px;top:22px">
        <div class="tile__label">Laundry &amp; Ironing</div>
        <div class="tile__photo" role="img" aria-label="Wardrobe with folded laundry" style="background:linear-gradient(180deg,#7a4a2a,#d9c7b0 55%,#6b4a33)"></div>
      </div>
      <div class="tile" style="left:323px;top:22px">
        <div class="tile__label">Oven Cleaning</div>
        <div class="tile__photo" role="img" aria-label="Kitchen with range cooker" style="background:linear-gradient(180deg,#e8e6e0,#cfcac2 50%,#1f2a2a)"></div>
      </div>
      <div class="tile" style="left:18px;top:138px">
        <div class="tile__label">Flower Arrangements</div>
        <div class="tile__photo" role="img" aria-label="Bouquet of pink roses and hydrangeas" style="background:linear-gradient(135deg,#f3c6d4,#d86aa6 50%,#f4e6c8)"></div>
      </div>
      <div class="tile" style="left:171px;top:138px">
        <div class="tile__label">Pet Food Delivery</div>
        <div class="tile__photo" role="img" aria-label="Two dogs on a lawn" style="background:linear-gradient(180deg,#8fb55a,#b0723a 55%,#7aa048)"></div>
      </div>
      <div class="tile" style="left:323px;top:138px">
        <div class="tile__label">Dry Cleaning</div>
        <div class="tile__photo" role="img" aria-label="Lace wedding gown on a balcony" style="background:linear-gradient(180deg,#c99a7c,#ece8e2 55%,#8a7a6c)"></div>
      </div>
    </div>

    <div class="contact-area">
      <address class="contact" style="font-style:normal">
        <span class="contact__tag">CONTACT</span>
        <p class="contact__address">Hollowmere Farm, Mill Lane, Ashcombe<br>Somerset TA9 4XY, GB</p>
        <p class="contact__phone">Tel: +44 7700 900412</p>
        <p class="contact__web">WWW.<span>HOLLOWMEREFARM</span>.EXAMPLE.CO.UK</p>
      </address>
    </div>
  </section>

</main>
</body>
</html>
```